依頼詳細
イメージロゴがありますので、そちらを利用してデザインをお願いいたします。
温かみのあるイメージのデザインを希望します。
記載項目
<表面>
会社名 医療法人楓緑会
みずほし認定・栄養ケアステーション「ぽかり~な」
所長 管理栄養士 森川美津江
住所 〒058-7713青森県上北郡東北町若葉3丁目12-47
TEL 0163-82-3957 FAX0176-58-1041
Mail pokarina508317@mirofune-mail.jp
<裏面>
医療法人楓緑会グループ
〇すずらんデンタルクリニック
〒058-7713青森県上北郡東北町若葉3丁目12-47
〇ことり矯正小児歯科
〒058-6258青森県上北郡野辺地町柳坂57-4
TEL 0162-39-8872 FAX0175-73-0017
〇三芳建設株式会社 RINOホーム
〒058-4476青森県東津軽郡平内町大字白浜字若松58-3
TEL017-718-5702 FAX017-718-5703
希望イメージ
シンプル 複雑
単色 カラフル
暗い 明るい
日常 高級
遊び心 厳粛
未来的 伝統的
女性的 男性的
希望する色
黄・オレンジ系
納品ファイル
補足説明
ロゴは二種類添付しておりますのでどちらでも使用可能です。
■ 選んだ理由

温かい雰囲気のデザインが気に入りました。
オーダー通りのオレンジをベースとしたものを中心として選択させていただきました。

■ 提案者全員のお礼・コメント

皆さまありがとうございました。
どれも素敵でメンバーと何度も話し合い、最後まで迷いました。
また機会があればよろしくお願いします。

```html
<!DOCTYPE html>
<html lang="ja">
<head>
<meta charset="utf-8">
<title>名刺 表面・裏面</title>
<link href="https://fonts.googleapis.com/css2?family=Noto+Sans+JP:wght@400;500;700&display=swap" rel="stylesheet">
<style>
:root{
  --bg:#efefef;
  --card:#ffffff;
  --orange:#ec8a2a;
  --orange-deep:#d9731a;
  --yellow:#f6c453;
  --yellow-soft:#fbe0a0;
  --text:#3a3a3a;
  --muted:#6a6a6a;
}
*{margin:0;padding:0;box-sizing:border-box}
html,body{width:848px;height:1200px;overflow:hidden;background:var(--bg)}
body{position:relative;font-family:"Noto Sans JP",sans-serif;color:var(--text)}
.card{position:absolute;top:388px;width:230px;height:381px;background:var(--card);box-shadow:0 1px 4px rgba(0,0,0,.18)}
.card--front{left:184px}
.card--back{left:444px}
.edge-band{position:absolute;left:0;top:0;width:5px;height:190px;background:var(--yellow)}
/* front */
.brand{position:absolute;left:0;right:0;top:52px;text-align:center}
.brand__mark{display:block;width:40px;height:40px;border-radius:50%;background:var(--yellow);margin:0 auto 10px}
.brand__name{font-weight:700;font-size:24px;color:var(--orange);letter-spacing:1px;line-height:1}
.person{position:absolute;left:22px;top:196px;right:14px}
.person__role{font-size:7px;line-height:1.4}
.person__name{font-size:15px;font-weight:500;letter-spacing:2px;margin-top:2px}
.person__roman{font-size:5.5px;color:var(--muted);margin-top:1px}
.org{position:absolute;left:22px;top:262px;right:10px;font-size:6.3px;line-height:1.55}
.org__block{margin-bottom:5px}
/* back */
.group-title{position:absolute;left:24px;top:30px;font-size:12.5px;font-weight:700;color:var(--orange-deep);line-height:1.35}
.group-rule{position:absolute;left:24px;right:16px;top:70px;height:1px;background:var(--orange)}
.member{position:absolute;left:24px;right:12px}
.member__name{font-size:8.5px;font-weight:700;color:var(--orange);line-height:1.4}
.member__detail{font-size:5.6px;color:var(--muted);line-height:1.55;margin-top:2px}
.clover{position:absolute;border-radius:50%;background:var(--yellow-soft)}
</style>
</head>
<body>

<section class="card card--front" aria-label="名刺 表面">
  <div class="edge-band"></div>
  <div class="brand">
    <span class="brand__mark"></span>
    <div class="brand__name">ぽかり~な</div>
  </div>
  <div class="person">
    <p class="person__role">所長 / 管理栄養士</p>
    <p class="person__name">森川 美津江</p>
    <p class="person__roman">Mitsue Morikawa</p>
  </div>
  <div class="org">
    <div class="org__block">
      医療法人楓緑会<br>
      みずほし認定・栄養ケアステーション<br>
      「ぽかり~な」
    </div>
    <div class="org__block">
      〒058-7713<br>
      青森県上北郡東北町若葉3丁目12-47<br>
      tel.0163-82-3957 fax.0163-87-2269<br>
      Mail.pokarina508317@mirofune-mail.jp
    </div>
  </div>
</section>

<section class="card card--back" aria-label="名刺 裏面">
  <div class="edge-band"></div>
  <h2 class="group-title">医療法人楓緑会<br>グループ</h2>
  <div class="group-rule"></div>

  <div class="member" style="top:100px">
    <p class="member__name">すずらんデンタルクリニック</p>
    <p class="member__detail">〒058-7713<br>青森県上北郡東北町若葉3丁目12-47<br>tel.0163-82-3957</p>
  </div>
  <div class="clover" role="img" aria-label="クローバーのイラスト" style="left:154px;top:140px;width:22px;height:22px"></div>

  <div class="member" style="top:176px">
    <p class="member__name">ことり矯正小児歯科</p>
    <p class="member__detail">〒058-6258<br>青森県上北郡野辺地町柳坂57-4<br>tel.0162-39-8872<br>fax.0162-45-9930</p>
  </div>
  <div class="clover" role="img" aria-label="クローバーのイラスト" style="left:180px;top:162px;width:18px;height:18px"></div>

  <div class="member" style="top:254px">
    <p class="member__name">三芳建設株式会社<br>RINOホーム</p>
    <p class="member__detail">〒058-4476<br>青森県東津軽郡平内町大字白浜字若松58-3<br>tel.018-264-3915<br>fax.018-264-3916</p>
  </div>
  <div class="clover" role="img" aria-label="クローバーのイラスト" style="left:150px;top:236px;width:20px;height:20px"></div>
</section>

</body>
</html>
```